Kestrel Signs Facebook Banner Design

Design a facebook banner for a sign company. I would like to have a modern approach to it.

Product Offering:
Signs
Banners
Decals
Commercial Wraps

```html
<!DOCTYPE html>
<html lang="en">
<head>
<meta charset="utf-8">
<title>Kestrel Signs – Facebook Banner</title>
<link href="https://fonts.googleapis.com/css2?family=Roboto:wght@400;700;900&display=swap" rel="stylesheet">
<style>
  :root {
    --panel: #f2f2f2;
    --ink: #4a4a4a;
    --red: #e8343f;
    --white: #ffffff;
    --gap: #e6e6e6;
  }
  * { margin: 0; padding: 0; box-sizing: border-box; }
  html, body { width: 1200px; height: 457px; overflow: hidden; background: var(--white); }
  .banner {
    position: relative;
    width: 1200px;
    height: 457px;
    background: var(--gap);
    font-family: "Roboto", Arial, sans-serif;
    overflow: hidden;
  }
  .intro {
    position: absolute;
    left: 0; top: 0;
    width: 612px; height: 457px;
    background: var(--panel);
  }
  .brand-name {
    position: absolute;
    left: 358px; top: 24px;
    color: var(--red);
    font-weight: 900;
    font-size: 30px;
    line-height: 31px;
    text-transform: uppercase;
    text-align: center;
    letter-spacing: 0.5px;
  }
  .headline {
    position: absolute;
    left: 46px; top: 92px;
    color: var(--ink);
    font-weight: 700;
    font-size: 56px;
    line-height: 66px;
    text-transform: uppercase;
    letter-spacing: 0.5px;
  }
  .headline .accent { color: var(--red); }
  .contacts {
    position: absolute;
    left: 46px; top: 318px;
    list-style: none;
  }
  .contacts li {
    display: flex;
    align-items: center;
    height: 38.5px;
    color: var(--ink);
    font-size: 22px;
    font-weight: 400;
  }
  .contacts svg {
    width: 26px; height: 26px;
    margin-right: 12px;
    fill: none;
    stroke: var(--red);
    stroke-width: 2;
    stroke-linecap: round;
    stroke-linejoin: round;
  }
  .tile {
    position: absolute;
    overflow: hidden;
  }
  .tile-photo { position: absolute; inset: 0; }
  .tile-signs { left: 612px; top: 0; width: 293px; height: 227px; }
  .tile-banners { left: 907px; top: 0; width: 293px; height: 227px; }
  .tile-decals { left: 612px; top: 230px; width: 293px; height: 227px; }
  .tile-wraps { left: 907px; top: 230px; width: 293px; height: 227px; }
  .tile-signs .tile-photo { background: linear-gradient(160deg, #d9d9d9 0%, #a9b4b8 45%, #5b4a44 100%); }
  .tile-banners .tile-photo { background: linear-gradient(170deg, #cfd2d5 0%, #7fa6c8 40%, #3a3f45 100%); }
  .tile-decals .tile-photo { background: linear-gradient(150deg, #5d6266 0%, #c9cdd0 45%, #2d3034 100%); }
  .tile-wraps .tile-photo { background: linear-gradient(150deg, #9aa0a4 0%, #2f3a2e 45%, #3f8a3a 75%, #1f2420 100%); }
  .tile::after {
    content: "";
    position: absolute;
    left: 0; right: 0; bottom: 0;
    height: 60%;
    background: linear-gradient(to bottom, rgba(0,0,0,0), rgba(0,0,0,0.55));
  }
  .tile-label {
    position: absolute;
    left: 0; right: 0; bottom: 62px;
    z-index: 1;
    color: var(--white);
    font-weight: 900;
    font-size: 32px;
    line-height: 36px;
    text-align: center;
    text-transform: uppercase;
    letter-spacing: 0.5px;
  }
  .tile-decals .tile-label { bottom: 12px; }
  .tile-wraps .tile-label { bottom: 8px; }
</style>
</head>
<body>
<div class="banner">
  <section class="intro">
    <div class="brand-name">Kestrel<br>Signs</div>
    <h1 class="headline">We are a<br><span class="accent">Signage</span><br>Company</h1>
    <ul class="contacts">
      <li>
        <svg viewBox="0 0 24 24" aria-hidden="true"><path d="M22 16.9v3a2 2 0 0 1-2.2 2 19.8 19.8 0 0 1-8.6-3.1 19.5 19.5 0 0 1-6-6A19.8 19.8 0 0 1 2.1 4.2 2 2 0 0 1 4.1 2h3a2 2 0 0 1 2 1.7c.1.9.4 1.8.7 2.7a2 2 0 0 1-.5 2.1L8 9.8a16 16 0 0 0 6 6l1.3-1.3a2 2 0 0 1 2.1-.4c.9.3 1.8.6 2.7.7a2 2 0 0 1 1.7 2z"/></svg>
        123 456 7890
      </li>
      <li>
        <svg viewBox="0 0 24 24" aria-hidden="true"><rect x="2" y="4" width="20" height="16" rx="2"/><path d="M2 6l10 7 10-7"/></svg>
        info@websitename.com
      </li>
      <li>
        <svg viewBox="0 0 24 24" aria-hidden="true"><circle cx="12" cy="12" r="10"/><path d="M2 12h20M12 2a15 15 0 0 1 0 20M12 2a15 15 0 0 0 0 20"/></svg>
        Www.websitename.com
      </li>
    </ul>
  </section>

  <div class="tile tile-signs">
    <div class="tile-photo" role="img" aria-label="Photo of a round hanging shop sign on an ornate iron bracket"></div>
    <span class="tile-label">Signs</span>
  </div>
  <div class="tile tile-banners">
    <div class="tile-photo" role="img" aria-label="Photo of a blue and white billboard banner on a tall post"></div>
    <span class="tile-label">Banners</span>
  </div>
  <div class="tile tile-decals">
    <div class="tile-photo" role="img" aria-label="Photo of a car side mirror with a football decal"></div>
    <span class="tile-label">Decals</span>
  </div>
  <div class="tile tile-wraps">
    <div class="tile-photo" role="img" aria-label="Photo of a van with a full green and black commercial vehicle wrap"></div>
    <span class="tile-label">Commercial<br>Wraps</span>
  </div>
</div>
</body>
</html>
```